Employee Wellbeing Model Graphic Design

A visual/graphic representation of our Employee Wellbeing model.
Our model is a combination of the Ngā Kiri Rehu Pona model of health and wellbeing and the wellbeing continuum.
We would like the visual to be on one page. The design should be modern and simple.
The powerpoint attached shows the information we are wanting to share with our employees about our wellbeing programme.

Target Market(s)

Our employees

Industry/Entity Type

Event Management

Font styles to use
Sans Serif
Other font styles liked:
• calibri light

Colors
00AB8E
00BBA5
67D7C9
C6EFE9
E9F9F6

```html
<!DOCTYPE html>
<html lang="en">
<head>
<meta charset="utf-8">
<title>Our Wellbeing Framework</title>
<link rel="stylesheet" href="https://fonts.googleapis.com/css2?family=Inter:wght@400;600;700;800&display=swap">
<style>
  :root {
    --page: #ffffff;
    --paper: #efefea;
    --ink: #222021;
    --house: #ecd1c6;
    --mental: #df3a42;
    --physical: #be4b3e;
    --family: #461646;
    --spirit: #222447;
    --land: #1f5b50;
    --unwell: #1aad4b;
    --struggling: #f6bb1a;
    --going-ok: #f1a1c5;
    --thriving: #663f9a;
    --ground: #5a4a3a;
    --white: #ffffff;
  }
  * { box-sizing: border-box; margin: 0; padding: 0; }
  html, body { width: 1200px; height: 1200px; overflow: hidden; background: var(--page); }
  body { position: relative; font-family: "Inter", Arial, sans-serif; }

  .framework {
    position: absolute; left: 0; top: 172px;
    width: 1659px; height: 1183px;
    transform: scale(0.7233); transform-origin: 0 0;
    background: var(--paper); overflow: hidden;
  }
  .framework__header {
    position: absolute; left: 35px; right: 35px; top: 28px;
    display: flex; align-items: center;
  }
  .framework__title {
    font-size: 66px; font-weight: 800; color: var(--ink); letter-spacing: -0.5px;
    white-space: nowrap; line-height: 1.2;
  }
  .framework__rule {
    flex: 1; height: 6px; background: var(--ink); margin-left: 28px; margin-top: 8px;
  }
  .roof { position: absolute; left: 0; top: 0; width: 1659px; height: 420px; }
  .roof__label {
    position: absolute; left: 728px; width: 200px; top: 232px; text-align: center;
    color: var(--white); font-size: 40px; font-weight: 700;
  }
  .house {
    position: absolute; left: 400px; top: 399px; width: 853px; height: 536px;
    background: var(--house); border: 2px solid var(--ink); border-top: none;
  }
  .pillar {
    position: absolute; left: 409px; width: 836px; height: 85px;
    display: flex; align-items: center; color: var(--white);
  }
  .pillar__icon { position: absolute; left: 151px; top: 12px; width: 62px; height: 62px; }
  .pillar__text { position: absolute; left: 243px; white-space: nowrap; }
  .pillar__name { font-size: 30px; font-weight: 700; }
  .pillar__meaning { font-size: 22px; font-weight: 400; margin-left: 8px; }
  .pillar--mental { top: 408px; background: var(--mental); }
  .pillar--physical { top: 501px; background: var(--physical); }
  .pillar--family { top: 593px; background: var(--family); }
  .pillar--spirit { top: 686px; background: var(--spirit); }
  .pillar--land { top: 779px; background: var(--land); }
  .house__name {
    position: absolute; left: 400px; width: 853px; top: 874px; text-align: center;
    font-size: 40px; font-weight: 700; color: var(--ink);
  }
  .base {
    position: absolute; left: 345px; top: 933px; width: 964px; height: 104px;
    background: var(--house); border: 2px solid var(--ink); border-bottom: none;
  }
  .continuum {
    position: absolute; left: 353px; top: 943px; width: 948px; height: 84px; display: flex;
  }
  .stage { position: relative; flex: 1; display: flex; align-items: center; color: var(--white); overflow: hidden; }
  .stage__icon { position: absolute; left: 38px; top: 18px; width: 48px; height: 48px; }
  .stage__label { position: absolute; left: 98px; font-size: 23px; font-weight: 700; white-space: nowrap; }
  .stage--unwell { background: var(--unwell); }
  .stage--struggling { background: var(--struggling); }
  .stage--going-ok { background: var(--going-ok); }
  .stage--thriving { background: var(--thriving); }
  .ground {
    position: absolute; left: 0; top: 1036px; width: 1659px; height: 147px;
    background: var(--ground); border-top: 2px solid var(--ink);
    display: flex; align-items: center; justify-content: center;
    color: var(--white); font-size: 46px; font-weight: 700; padding-bottom: 36px;
  }
  .icon-slot { display: block; }
</style>
</head>
<body>
<main class="framework">
  <header class="framework__header">
    <h1 class="framework__title">Our Wellbeing Framework</h1>
    <div class="framework__rule"></div>
  </header>

  <svg class="roof" viewBox="0 0 1659 420" aria-hidden="true">
    <path fill="#222021" d="M828 171 L1049 278 L1049 268 Q1049 248 1069 248 L1130 248 Q1150 248 1150 268 L1150 326 L1299 399 L355 399 Z"/>
  </svg>
  <div class="roof__label">Pou</div>

  <div class="house"></div>

  <div class="pillar pillar--mental">
    <svg class="pillar__icon icon-slot" viewBox="0 0 62 62" role="img" aria-label="Head with brain icon"><circle cx="31" cy="31" r="24" fill="none" stroke="#fff" stroke-width="2.5"/></svg>
    <p class="pillar__text"><span class="pillar__name">Taha Hinegaro -</span><span class="pillar__meaning">Mental/Emotional Health</span></p>
  </div>
  <div class="pillar pillar--physical">
    <svg class="pillar__icon icon-slot" viewBox="0 0 62 62" role="img" aria-label="Person icon">
      <g fill="none" stroke="#fff" stroke-width="2.5" stroke-linejoin="round">
        <circle cx="31" cy="9" r="6"/>
        <path d="M22 19 h18 v20 h-4 v20 h-10 v-20 h-4 Z M31 39 v20"/>
      </g>
    </svg>
    <p class="pillar__text"><span class="pillar__name">Tana Tinana -</span><span class="pillar__meaning">Physical Health</span></p>
  </div>
  <div class="pillar pillar--family">
    <svg class="pillar__icon icon-slot" viewBox="0 0 62 62" role="img" aria-label="Community care icon">
      <g fill="none" stroke="#fff" stroke-width="2.5">
        <circle cx="31" cy="31" r="13"/>
        <path d="M31 24 v14 M24 31 h14"/>
        <circle cx="9" cy="8" r="4"/><circle cx="53" cy="8" r="4"/><circle cx="9" cy="50" r="4"/><circle cx="53" cy="50" r="4"/>
      </g>
    </svg>
    <p class="pillar__text"><span class="pillar__name">Taha Whanau -</span><span class="pillar__meaning">Family/Community Health</span></p>
  </div>
  <div class="pillar pillar--spirit">
    <svg class="pillar__icon icon-slot" viewBox="0 0 62 62" role="img" aria-label="Meditation lotus icon"><circle cx="31" cy="31" r="24" fill="none" stroke="#fff" stroke-width="2.5"/></svg>
    <p class="pillar__text"><span class="pillar__name">Taha Wairua -</span><span class="pillar__meaning">Spiritual Health</span></p>
  </div>
  <div class="pillar pillar--land">
    <svg class="pillar__icon icon-slot" viewBox="0 0 62 62" role="img" aria-label="Roots icon"><circle cx="31" cy="31" r="24" fill="none" stroke="#fff" stroke-width="2.5"/></svg>
    <p class="pillar__text"><span class="pillar__name">Whenua -</span><span class="pillar__meaning">Land/Roots</span></p>
  </div>

  <p class="house__name">Ngā Kiri Rehu Pona</p>

  <div class="base"></div>
  <div class="continuum">
    <div class="stage stage--unwell">
      <svg class="stage__icon" viewBox="0 0 48 48" aria-hidden="true">
        <g fill="none" stroke="#fff" stroke-width="2.5">
          <circle cx="24" cy="24" r="21"/>
          <path d="M24 11 v17" stroke-linecap="round" stroke-width="4"/>
          <circle cx="24" cy="35" r="2" fill="#fff"/>
        </g>
      </svg>
      <span class="stage__label">Unwell</span>
    </div>
    <div class="stage stage--struggling">
      <svg class="stage__icon" viewBox="0 0 48 48" role="img" aria-label="Stressed head icon"><circle cx="24" cy="24" r="20" fill="none" stroke="#fff" stroke-width="2.5"/></svg>
      <span class="stage__label">Struggling</span>
    </div>
    <div class="stage stage--going-ok">
      <svg class="stage__icon" viewBox="0 0 48 48" aria-hidden="true">
        <g fill="none" stroke="#fff" stroke-width="2.5" stroke-linejoin="round">
          <path d="M4 22 h8 v20 h-8 Z M12 24 l8 -12 q3 -4 5 0 l-2 9 h12 q4 0 3 4 l-3 14 q-1 3 -4 3 h-19"/>
          <circle cx="39" cy="10" r="7"/>
          <path d="M36 10 l2 2 l4 -4"/>
        </g>
      </svg>
      <span class="stage__label">Going OK</span>
    </div>
    <div class="stage stage--thriving">
      <svg class="stage__icon" viewBox="0 0 48 48" role="img" aria-label="Heart and raised hands icon"><circle cx="24" cy="24" r="20" fill="none" stroke="#fff" stroke-width="2.5"/></svg>
      <span class="stage__label">Thriving</span>
    </div>
  </div>

  <footer class="ground">The Wellbeing Continuum</footer>
</main>
</body>
</html>
```